Flat Belly Design Graphics for Social

I want to create 9 social media graphics (new Instagram size 4:5 (1080 x 1350 pixels) focusing on our Flat Belly Graphics, using the pics attached. Use the attached pics, NO RANDOM STOCK PHOTOGRAPHY. For the color scheme of the graphics, the color palette is attached. YOU MUST POST ALL 9 GRAPHICS IN ONE ENTRY.
Using the 3 titles below, create one set of graphics. 1) with all text, then for the others, use the pictures as detailed below in IMPORTANT:
1. 21-Night Lean Middle Reboot Beyond 50
2. The 20-Second Trim-Core Menu Guide
3. Starlet Tricks to a Slender Midline Beyond 50 - Zero Scalpel Needed
IMPORTANT:
Only use RK Pic 1 and RK Pic 2 with the title, 21-Night Lean Middle Reboot Beyond 50
Only use meal plan1 and meal plan2 pics with the title, 20-Second Trim-Core Menu Guide
Only use starlet tricks 1 and starlet tricks 2 pics with the title, Starlet Tricks to a Slender Midline Beyond 50 - Zero Scalpel Needed
women over 40

```html
<!DOCTYPE html>
<html lang="en">
<head>
<meta charset="utf-8">
<title>Lean Middle Social Set</title>
<link rel="stylesheet" href="https://fonts.googleapis.com/css2?family=Montserrat:wght@200;600;700;800;900&display=swap">
<style>
  :root {
    --forest: #374b4a;
    --rose: #d99aae;
    --blush: #f8e9ed;
    --white: #ffffff;
    --page: #ffffff;
  }
  * { margin: 0; padding: 0; box-sizing: border-box; }
  html, body { width: 961px; height: 1200px; overflow: hidden; background: var(--page); }
  body { font-family: "Montserrat", Arial, sans-serif; font-weight: 800; position: relative; }

  .grid { position: absolute; left: 87px; top: 117px; width: 767px; height: 960px; }
  .tile { position: absolute; overflow: hidden; width: 255px; height: 319px; }
  .c1 { left: 0; } .c2 { left: 258px; width: 252px; } .c3 { left: 513px; width: 254px; }
  .r1 { top: 0; } .r2 { top: 322px; } .r3 { top: 643px; height: 317px; }

  .bg-forest { background: var(--forest); }
  .bg-rose { background: var(--rose); }

  .photo { position: absolute; }
  .line { position: absolute; white-space: nowrap; line-height: 1; letter-spacing: -0.5px; }
  .box { padding: 2px 5px; }
  .t-forest { color: var(--forest); } .t-rose { color: var(--rose); } .t-white { color: var(--white); }
  .b-forest { background: var(--forest); } .b-rose { background: var(--rose); }
  .b-white { background: var(--white); } .b-blush { background: var(--blush); }
  .outline-white { color: transparent; -webkit-text-stroke: 1.4px var(--white); font-weight: 200; }
  .outline-forest { color: transparent; -webkit-text-stroke: 1.4px var(--forest); font-weight: 200; }
  .right { text-align: right; }
</style>
</head>
<body>
<main class="grid">

  <!-- Row 1: Reboot -->
  <section class="tile c1 r1 reboot-photo-left">
    <div class="photo" role="img" aria-label="Smiling woman in a white cropped sweater pointing at her midsection in a kitchen" style="inset:0;background:linear-gradient(180deg,#6b5246 0%,#a07a63 45%,#5a4a42 75%,var(--forest) 100%);"></div>
    <div class="line box" style="left:0;top:216px;background:rgba(210,210,210,.75);color:#3a3a3a;font-size:27px;">21-NIGHT</div>
    <div class="line t-white" style="left:8px;top:262px;font-size:22px;">LEAN MIDDLE</div>
    <div class="line t-white" style="left:10px;top:288px;font-size:22px;">reboot <span class="t-rose">BEYOND 50</span></div>
  </section>

  <section class="tile c2 r1 bg-rose reboot-type">
    <div class="line box b-blush t-forest" style="left:51px;top:43px;font-size:31px;">21-NIGHT</div>
    <div class="line t-white" style="left:51px;top:94px;font-size:56px;">LEAN</div>
    <div class="line t-forest" style="left:51px;top:145px;font-size:33px;">MIDDLE</div>
    <div class="line t-white" style="left:51px;top:184px;font-size:20px;">REBOOT</div>
    <div class="line box b-forest t-white" style="left:51px;top:208px;font-size:20px;">BEYOND</div>
    <div class="line t-white" style="left:49px;top:240px;font-size:62px;">50</div>
  </section>

  <section class="tile c3 r1 reboot-photo-right" style="background:linear-gradient(90deg,var(--forest) 0 55%,var(--blush) 55% 100%);">
    <div class="photo" role="img" aria-label="Smiling woman in a white cropped sweater and black jeans pointing at her waist" style="left:0;top:0;width:230px;height:319px;background:linear-gradient(180deg,#2b2b2b 0%,#c9a58f 25%,#f2f0ef 45%,#c59a7f 70%,#1f1f1f 100%);opacity:.9;"></div>
    <div class="line outline-forest right" style="right:6px;top:18px;font-size:66px;">21</div>
    <div class="line t-forest right" style="right:6px;top:82px;font-size:30px;">NIGHT</div>
    <div class="line t-rose right" style="right:6px;top:114px;font-size:34px;">LEAN</div>
    <div class="line t-forest right" style="right:6px;top:150px;font-size:32px;">MIDDLE</div>
    <div class="line box b-forest t-white right" style="right:56px;top:184px;font-size:20px;">REBOOT</div>
    <div class="line box b-forest t-white right" style="right:2px;top:240px;font-size:20px;">BEYOND</div>
    <div class="line t-rose right" style="right:8px;top:270px;font-size:44px;">50</div>
  </section>

  <!-- Row 2: Menu guide -->
  <section class="tile c1 r2 bg-forest menu-type">
    <div class="line t-rose" style="left:42px;top:38px;font-size:20px;">THE</div>
    <div class="line outline-white" style="left:40px;top:58px;font-size:60px;">20</div>
    <div class="line t-white" style="left:42px;top:118px;font-size:22px;">SECOND</div>
    <div class="line t-rose" style="left:44px;top:144px;font-size:48px;">TRIM-</div>
    <div class="line t-rose" style="left:42px;top:190px;font-size:48px;">CORE</div>
    <div class="line box b-white t-forest" style="left:42px;top:243px;font-size:26px;">MENU GUIDE</div>
  </section>

  <section class="tile c2 r2 bg-forest menu-photo-left">
    <div class="photo" role="img" aria-label="Overhead spread of vegetables, tomatoes, avocado, salmon, eggs and lentils on dark wood" style="left:60px;top:0;right:0;bottom:0;background:linear-gradient(135deg,#5a3d2a 0%,#b8412f 30%,#7d8a3a 50%,#e07d5a 70%,#3d2a20 100%);"></div>
    <div class="line t-white" style="left:28px;top:45px;font-size:22px;writing-mode:vertical-rl;transform:rotate(180deg);letter-spacing:6px;">THE</div>
    <div class="line box b-rose t-white" style="left:52px;top:48px;font-size:60px;padding:2px 4px;">20</div>
    <div class="line t-rose" style="left:26px;top:122px;font-size:26px;">SECOND</div>
    <div class="line t-white" style="left:26px;top:148px;font-size:42px;">TRIM-</div>
    <div class="line t-white" style="left:26px;top:188px;font-size:42px;">CORE</div>
    <div class="line box b-white t-rose" style="left:28px;top:238px;font-size:26px;">MENU GUIDE</div>
  </section>

  <section class="tile c3 r2 menu-photo-right">
    <div class="photo" role="img" aria-label="Raw chicken breast, tomatoes, asparagus and a meal planner notepad on a wooden table" style="inset:0;background:linear-gradient(160deg,#f1c9b5 0%,#c9836b 35%,#6b7f3a 60%,#4a3628 80%,#d7d7d7 100%);"></div>
    <div class="line t-white right" style="right:10px;top:16px;font-size:20px;">THE</div>
    <div class="line t-white right" style="right:10px;top:36px;font-size:48px;">20</div>
    <div class="line t-white right" style="right:10px;top:90px;font-size:22px;">SECOND</div>
    <div class="line box b-rose t-white" style="left:12px;top:117px;font-size:33px;">TRIM-CORE</div>
    <div class="line box b-white t-forest" style="right:10px;top:167px;font-size:20px;">MENU GUIDE</div>
  </section>

  <!-- Row 3: Starlet tricks -->
  <section class="tile c1 r3 tricks-photo-left">
    <div class="photo" role="img" aria-label="Two women sharing a whispered secret, one looking surprised" style="inset:0;background:linear-gradient(180deg,#3a2a24 0%,#a8755c 35%,#d99aae 60%,var(--forest) 80%);"></div>
    <div class="line t-white" style="left:20px;top:185px;font-size:28px;">STARLET</div>
    <div class="line t-rose" style="left:20px;top:210px;font-size:30px;">TRICKS</div>
    <div class="line t-white" style="left:24px;top:242px;font-size:16px;"><span style="font-size:9px;">TO </span>A SLENDER MIDLINE</div>
    <div class="line box b-rose t-white" style="left:22px;top:264px;font-size:20px;">BEYOND 50</div>
    <div class="line t-rose" style="left:25px;top:294px;font-size:15px;">ZERO SCALPEL <span class="t-white">NEEDED</span></div>
  </section>

  <section class="tile c2 r3 bg-forest tricks-photo-right">
    <div class="photo" role="img" aria-label="Surprised woman listening as a friend whispers to her, pink backdrop" style="inset:0;background:linear-gradient(120deg,#c4907d 0%,#e8c3b3 35%,#d99aae 60%,#6b4a3c 80%,#4d6fa0 100%);"></div>
    <div class="line box b-rose t-white" style="left:12px;top:136px;font-size:19px;">STARLET TRICKS</div>
    <div class="line t-white" style="left:20px;top:168px;font-size:10px;letter-spacing:5px;">TO</div>
    <div class="line t-white" style="left:20px;top:180px;font-size:24px;">A SLENDER</div>
    <div class="line t-white" style="left:20px;top:203px;font-size:24px;">MIDLINE</div>
    <div class="line box b-rose t-forest" style="left:16px;top:232px;font-size:20px;">BEYOND 50</div>
    <div class="line t-forest" style="left:18px;top:293px;font-size:15px;">ZERO SCALPEL <span class="t-white">NEEDED</span></div>
  </section>

  <section class="tile c3 r3 bg-rose tricks-type">
    <div class="line t-forest" style="left:33px;top:52px;font-size:32px;">STARLET</div>
    <div class="line t-white" style="left:33px;top:88px;font-size:36px;">TRICKS</div>
    <div class="line t-forest" style="left:33px;top:132px;font-size:18px;">TO</div>
    <div class="line box b-white t-forest" style="left:33px;top:157px;font-size:18px;">A SLENDER MIDLINE</div>
    <div class="line t-white" style="left:33px;top:190px;font-size:31px;">BEYOND 50</div>
    <div class="line box b-forest t-white" style="left:33px;top:226px;font-size:22px;">ZERO SCALPEL</div>
    <div class="line box b-forest t-white" style="left:33px;top:253px;font-size:22px;">NEEDED</div>
  </section>

</main>
</body>
</html>
```